Business cards

Design business cards for our company. Just a straight, business like design with the logo, name, function and contact details

Target Market(s)

We are a innovative technological company active in water treatment

Industry/Entity Type

Water management

Contact Information for Business Card

Name, Function, email, telephone number, link to website

```html
<!DOCTYPE html>
<html lang="en">
<head>
<meta charset="utf-8">
<title>Aquelion 7 — Business Cards</title>
<link href="https://fonts.googleapis.com/css2?family=Exo+2:wght@300;400;500&display=swap" rel="stylesheet">
<style>
  :root {
    --backdrop: #898c91;
    --card-white: #f7f7f8;
    --card-white-shade: #e9eaec;
    --brand-blue: #35a8e0;
    --brand-blue-light: #4fb6e6;
    --text-grey: #8e9093;
    --text-white: #ffffff;
  }
  * { box-sizing: border-box; margin: 0; padding: 0; }
  html, body {
    width: 1200px;
    height: 900px;
    overflow: hidden;
    background: var(--backdrop);
    font-family: "Exo 2", sans-serif;
  }
  .sheet {
    position: relative;
    width: 1200px;
    height: 900px;
  }
  .card {
    position: absolute;
    top: 300px;
    width: 500px;
    height: 300px;
    border-radius: 28px;
    overflow: hidden;
  }
  .card--front {
    left: 70px;
    background: radial-gradient(circle at 75% 60%, var(--card-white) 0%, var(--card-white-shade) 100%);
    padding: 38px 40px;
  }
  .card--back {
    left: 630px;
    background: linear-gradient(135deg, var(--brand-blue) 0%, var(--brand-blue-light) 60%, var(--brand-blue) 100%);
    display: flex;
    align-items: center;
    justify-content: center;
  }
  .brand {
    display: inline-flex;
    align-items: center;
    gap: 10px;
  }
  .brand__dot {
    width: 14px;
    height: 14px;
    border-radius: 50%;
    background: var(--brand-blue);
  }
  .brand__name {
    font-size: 34px;
    font-weight: 400;
    letter-spacing: 1px;
    color: var(--brand-blue);
    line-height: 1;
  }
  .brand__tagline {
    font-size: 10px;
    font-weight: 300;
    letter-spacing: 1.6px;
    text-transform: uppercase;
    color: var(--text-grey);
    margin-top: 4px;
  }
  .card--back .brand__dot { background: var(--text-white); width: 18px; height: 18px; }
  .card--back .brand__name { color: var(--text-white); font-size: 46px; }
  .card--back .brand__tagline { color: var(--text-white); font-size: 12px; letter-spacing: 2.4px; }
  .person { margin-top: 34px; }
  .person__name {
    font-size: 17px;
    font-weight: 400;
    letter-spacing: 1.5px;
    text-transform: uppercase;
    color: var(--brand-blue);
  }
  .person__role {
    font-size: 12px;
    font-weight: 300;
    letter-spacing: 1px;
    color: var(--text-grey);
    margin-top: 2px;
  }
  .contact { list-style: none; margin-top: 22px; }
  .contact__item {
    display: flex;
    align-items: center;
    gap: 8px;
    font-size: 13px;
    font-weight: 300;
    letter-spacing: 1.2px;
    color: var(--text-grey);
    line-height: 1.7;
  }
  .contact__icon { width: 10px; height: 10px; fill: var(--brand-blue); flex: none; }
</style>
</head>
<body>
  <main class="sheet">
    <section class="card card--front" aria-label="Card front">
      <div class="brand-block">
        <div class="brand">
          <span class="brand__name">Aquelion 7</span>
          <span class="brand__dot"></span>
        </div>
        <p class="brand__tagline">Nanobubble Technology</p>
      </div>
      <div class="person">
        <p class="person__name">Elias Moreno</p>
        <p class="person__role">Director</p>
      </div>
      <ul class="contact">
        <li class="contact__item">
          <svg class="contact__icon" viewBox="0 0 10 10"><path d="M2 0.5 L3.8 2.6 L2.9 3.8 Q3.9 5.9 6.2 7.1 L7.4 6.2 L9.5 8 L8.3 9.5 Q1.5 8.5 0.5 1.7 Z"/></svg>
          07900412358
        </li>
        <li class="contact__item">
          <svg class="contact__icon" viewBox="0 0 10 10"><path d="M0.5 2 H9.5 V8 H0.5 Z M0.5 2 L5 5.5 L9.5 2" fill="none" stroke="#35a8e0" stroke-width="1.2"/></svg>
          info@www.aquelion7.com
        </li>
        <li class="contact__item">
          <svg class="contact__icon" viewBox="0 0 10 10"><circle cx="5" cy="5" r="4.2" fill="none" stroke="#35a8e0" stroke-width="1.1"/><path d="M0.8 5 H9.2 M5 0.8 Q2.4 5 5 9.2 M5 0.8 Q7.6 5 5 9.2" fill="none" stroke="#35a8e0" stroke-width="0.9"/></svg>
          www.aquelion7.com
        </li>
      </ul>
    </section>

    <section class="card card--back" aria-label="Card back">
      <div class="brand-block">
        <div class="brand">
          <span class="brand__name">Aquelion 7</span>
          <span class="brand__dot"></span>
        </div>
        <p class="brand__tagline">Nanobubble Technology</p>
      </div>
    </section>
  </main>
</body>
</html>
```